Hearth & Keg Room requires web site design - Casual restaurant

Need website designed for re-branding of Restaurant based in Fort Morgan, Colorado. We offer a wide variety of American cuisine in a casual, rustic atmosphere. We're offering 16 craft beers on draft, as well as a full service bar, and modern, interesting menu selections in a friendly, fun and energetic environment, with an emphasis on superior customer service and high quality, locally sourced food. We are a family, and community service oriented establishment. The website design should convey a welcoming sense, "simplicity", yet sophisticated - without pretentiousness. The website should effectively convey our "home style" relaxed atmosphere, as well as our casual character.

Business Hours: Sunday - Thursday, 11am-10pm / Friday & Saturday, 11am-11am

The Dunlo Hearth & Keg Room
2736 Pennick Road
Alder Springs, Colorado 80799
B: (970) 555-0173

WEBSITE ADDRESS: thedunlokegroom.com

Target Market(s)

Young Adults
Families
Blue and White Collar Americans
Senior Citizens
Small town location, appeal to everyone

Industry/Entity Type

American Restaurant

Contact Information for Business Card

Marcus T Ellery
Food & Beverage Director
2736 Pennick Road
B: (970) 555-0173
M: (231) 555-0148
mtellery@dunlokegroom.com
www.thedunlokegroom.com
***Use logo in uploaded files
***Open to single OR double sided
*** I will have additional names and information to add to this, for other employees.

Coding

Coded - Design and coding required

Number of Pages Required

5+ page

Font styles to use
Serif
Sans Serif
Decorative
Other font styles liked:
• Calafornian FB,

Requirements
Must have
• Home/Welcome Page
• Menu Page/Online Ordering Ready
• About Us/Contact Us page
• Catering/Private Events/Banquets Advertising section
• Ability to link to Friendbook/TripAdvisor/Yelp/Instagram etc.
• Logo uploaded, reference for colors as well.
Nice to have
• About craft beer page
• Our Story/Bio section
• Photo Gallery
• Employment/Apply section
Should not have
• We are NOT a "fine dining" restaurant... think casual...

```html
<!DOCTYPE html>
<html lang="en">
<head>
<meta charset="utf-8">
<title>The Dunlo Hearth &amp; Keg Room</title>
<link rel="stylesheet" href="https://fonts.googleapis.com/css2?family=Raleway:ital,wght@0,300;0,400;0,600;0,700;1,400;1,600&family=Open+Sans:wght@400;600;700&family=Oswald:wght@400;600&display=swap">
<style>
:root{
  --orange:#e0531c;
  --ink:#222;
  --text:#555;
  --footer:#232323;
  --brown-1:#8a4318;
  --brown-2:#5e2a0e;
  --white:#fff;
}
*{box-sizing:border-box;margin:0;padding:0}
html,body{width:1200px;height:5279px;overflow:hidden}
body{font-family:"Open Sans",Arial,sans-serif;color:var(--text);background:var(--white);position:relative}
section,header,footer{position:relative;width:1200px;overflow:hidden}
.abs{position:absolute}
.photo{position:absolute}
h2.section-title{font-family:"Raleway",Helvetica,sans-serif;font-weight:300;font-size:40px;color:var(--ink)}
.rule{display:block;width:60px;height:2px;background:var(--orange);margin-top:10px}
.btn{display:inline-block;background:var(--orange);color:var(--white);font-family:"Raleway",sans-serif;font-weight:600;font-size:16px;border-radius:24px;text-align:center;text-decoration:none}

/* hero */
.hero{height:640px;background:linear-gradient(115deg,#3a2418 0%,#7b4a2a 35%,#b07a47 55%,#4a2b1a 80%,#2a1a12 100%)}
.hero .photo{inset:0}
.sidebar{position:absolute;left:0;top:0;width:232px;height:640px;background:rgba(10,10,10,.92)}
.brand{position:absolute;left:24px;top:40px;display:flex;align-items:center;gap:12px}
.brand-mark{width:26px;height:26px;background:var(--orange)}
.brand-name{font-family:"Raleway",sans-serif;font-weight:700;font-size:34px;color:var(--white);line-height:1}
.brand-sub{position:absolute;left:24px;top:86px;font-family:"Raleway",sans-serif;font-weight:700;font-size:13px;color:var(--white);letter-spacing:.5px}
.main-nav{position:absolute;left:32px;top:236px;list-style:none}
.main-nav li{font-family:"Raleway",sans-serif;font-size:15px;color:var(--white);height:40px;letter-spacing:.3px}
.social-dots{position:absolute;left:24px;top:548px;display:flex;gap:10px}
.social-dots span{width:34px;height:34px;border-radius:50%;background:var(--white)}
.topbar{position:absolute;left:232px;top:0;width:968px;height:50px;background:rgba(20,20,20,.85);display:flex;align-items:center;padding:0 40px 0 78px;color:var(--white);font-size:12px}
.topbar .hours{line-height:1.35;width:300px}
.topbar .phone{margin-left:auto;font-size:13px;display:flex;align-items:center;gap:8px}
.topbar .phone strong{font-size:17px}
.topbar .btn{margin-left:36px;font-size:12px;padding:7px 18px;text-transform:uppercase}
.hero-copy{position:absolute;left:264px;top:500px;width:800px;color:var(--white)}
.hero-copy h1{font-family:"Raleway",sans-serif;font-weight:600;font-size:46px;line-height:1}
.hero-copy h1 em{font-style:normal;color:var(--orange)}
.hero-copy p{font-size:17px;line-height:1.35;margin-top:10px}

/* story */
.story{height:480px}
.story h2{position:absolute;left:78px;top:68px}
.story .body{position:absolute;left:78px;top:150px;width:520px;font-size:14px;line-height:1.55}
.story .body b{color:var(--ink)}
.story .btn{position:absolute;left:78px;top:388px;width:180px;height:42px;line-height:42px}
.story .photo{left:626px;top:64px;width:494px;height:346px;border:6px solid #f4efe7;box-shadow:0 0 0 1px #ccc;background:linear-gradient(135deg,#5a3f2c,#c59a6a 45%,#f0d8b0 60%,#6b4a33)}

/* about */
.about{height:506px;background:linear-gradient(90deg,var(--brown-1),var(--brown-2) 50%,var(--brown-1))}
.about h2{font-family:"Raleway",sans-serif;font-weight:300;font-size:38px;color:var(--white);position:absolute;top:70px}
.about .copy{position:absolute;top:140px;width:260px;font-size:13px;line-height:1.5;color:#f3e4d8}
.about .copy p+p{margin-top:16px}
.about .left{left:78px}
.about .right{right:74px;text-align:right}
.about .photo{top:76px;width:218px;height:354px;border:4px solid var(--white);background:linear-gradient(180deg,#d9d4cf,#a89f98)}

/* menu */
.menu{color:var(--text)}
.menu-drinks{height:539px;background:linear-gradient(90deg,#efe9e4,#f7f3ef 50%,#e9e2db)}
.menu-drinks h2{position:absolute;top:62px;width:100%;text-align:center}
.menu-drinks .rule{position:absolute;left:570px;top:118px;margin:0}
.cat{font-family:"Raleway",sans-serif;font-style:italic;font-weight:600;font-size:26px;color:var(--orange);position:absolute;left:78px}
.item{position:absolute;width:460px}
.item h4{font-family:"Raleway",sans-serif;font-weight:600;font-size:15px;color:var(--ink);display:flex;align-items:center;gap:10px}
.item h4::before{content:"";width:14px;height:2px;background:var(--orange);display:inline-block}
.item p{font-size:12px;line-height:1.45;margin-left:34px;width:320px;margin-top:2px}
.item .price{position:absolute;right:0;top:12px;font-size:19px;color:var(--orange)}
.promo{position:absolute;border:2px solid var(--orange);padding:4px}
.promo-inner{border:1px solid var(--orange);height:100%;display:flex;align-items:center;padding:0 22px;gap:18px}
.promo .big{font-family:"Oswald",sans-serif;font-size:92px;line-height:1;color:var(--orange);position:relative}
.promo .big small{font-size:26px;position:absolute;top:6px;right:-26px}
.promo .dollar{flex:none;width:54px;height:54px;border:2px solid var(--orange);border-radius:50%;display:flex;align-items:center;justify-content:center;color:var(--orange);font-family:"Oswald",sans-serif;font-size:30px}
.promo h3{font-family:"Oswald",sans-serif;font-weight:600;font-size:23px;color:var(--orange);letter-spacing:.3px;white-space:nowrap}
.promo .line{font-family:"Oswald",sans-serif;font-size:15px;color:var(--orange)}
.promo .strong{font-family:"Oswald",sans-serif;font-size:15px;color:var(--ink);margin-top:4px;letter-spacing:.3px;line-height:1.35}
.chevron{position:absolute;left:578px;width:44px;height:44px;border-radius:50%;background:var(--white);box-shadow:0 1px 4px rgba(0,0,0,.25);display:flex;align-items:center;justify-content:center}
.menu-lunch{height:440px;background:linear-gradient(90deg,#2b1c14,#4a3020 50%,#2b1c14)}
.menu-lunch .item h4{color:var(--white)}
.menu-lunch .item p{color:#d6c8bd}
.menu-lunch .promo h3,.menu-lunch .promo .strong{color:var(--white)}
.menu-dinner{height:635px;background:var(--white)}
.menu-dinner .btn{position:absolute;left:510px;top:488px;width:180px;height:44px;line-height:44px;font-size:15px}

/* gallery */
.gallery{height:667px}
.gallery .photo{width:400px;height:334px}
.gallery-badge{position:absolute;left:495px;top:217px;width:210px;height:210px;border-radius:50%;background:#111;display:flex;flex-direction:column;align-items:center;justify-content:center;color:var(--white);font-family:"Raleway",sans-serif}
.gallery-badge .s{font-size:14px;color:var(--orange)}
.gallery-badge .l{font-size:36px;margin:2px 0}
.gallery-badge .m{font-size:14px}

/* features */
.features{height:451px;background:linear-gradient(90deg,#a9481a,#7a3110 50%,#a9481a)}
.feature{position:absolute;top:140px;width:330px;text-align:center;color:var(--white)}
.feature svg{display:block;margin:0 auto}
.feature h3{font-family:"Raleway",sans-serif;font-weight:400;font-size:22px;margin-top:14px}
.feature p{font-size:12px;line-height:1.5;color:#f3ddd0;margin-top:6px}

/* reviews */
.reviews{height:517px;background:linear-gradient(90deg,#ece7e3,#f7f4f1 50%,#ebe5df)}
.reviews h2{position:absolute;top:54px;width:100%;text-align:center}
.reviews .rule{position:absolute;left:570px;top:110px;margin:0}
.reviews .avatar{position:absolute;left:537px;top:155px;width:126px;height:126px;border-radius:50%;border:4px solid var(--white);background:linear-gradient(180deg,#c9b8a8,#6d5646)}
.stars{position:absolute;top:308px;width:100%;text-align:center;font-size:20px;color:var(--orange);letter-spacing:4px}
.stars span{color:#bbb}
.reviewer{position:absolute;top:346px;width:100%;text-align:center;font-family:"Raleway",sans-serif;font-size:16px;color:var(--orange)}
.quote{position:absolute;left:150px;top:386px;width:900px;text-align:center;font-size:14px;line-height:1.7;color:#444}
.qmark{position:absolute;font-family:Georgia,serif;font-size:64px;color:#333;line-height:1}

/* footer */
.site-footer{height:404px;background:var(--footer);color:#bbb}
.fcol{position:absolute;top:70px;font-size:12px;line-height:1.7}
.fcol h4{font-family:"Raleway",sans-serif;font-weight:400;font-size:18px;color:var(--white);margin-bottom:16px}
.fcol ul{list-style:none}
.fcol li::before{content:"› ";color:var(--orange)}
.contact-row{display:flex;gap:10px;margin-bottom:10px}
.contact-row svg{flex:none;margin-top:3px}
.signup{display:flex;margin-top:14px}
.signup span{display:block;width:190px;height:30px;background:var(--white);color:#999;font-size:12px;line-height:30px;padding-left:10px}
.signup-btn{display:block;margin-top:10px;width:90px;height:28px;line-height:28px;background:var(--orange);color:var(--white);text-align:center;font-size:12px}
.follow li{list-style:none;display:flex;align-items:center;gap:12px;margin-bottom:12px}
.follow li::before{content:none}
.follow i{width:24px;height:24px;background:var(--orange);display:block}
.copyright{position:absolute;left:0;bottom:0;width:1200px;height:34px;line-height:34px;background:#5a2a12;color:#e9cdbb;text-align:center;font-size:12px}
</style>
</head>
<body>

<header class="hero">
  <div class="photo" role="img" aria-label="Friends laughing and toasting with glasses of beer at the bar"></div>
  <aside class="sidebar">
    <div class="brand"><span class="brand-mark"></span><span class="brand-name">The Dunlo</span></div>
    <div class="brand-sub">Hearth &amp; Keg Room</div>
    <ul class="main-nav">
      <li>HOME</li><li>OUR STORY</li><li>OUR MENU</li><li>OUR GALLERY</li><li>CUSTOMER REVIEWS</li><li>CONTACT US</li>
    </ul>
    <div class="social-dots" aria-label="Social links"><span></span><span></span><span></span><span></span></div>
  </aside>
  <div class="topbar">
    <div class="hours">We're Open Sunday - Thursday: 11:00am - 10:00pm<br>Friday &amp; Saturday: 11:00am - 11:00pm</div>
    <div class="phone">
      <svg width="16" height="16" viewBox="0 0 24 24"><path fill="#fff" d="M6.6 10.8a15 15 0 0 0 6.6 6.6l2.2-2.2a1 1 0 0 1 1-.25 11 11 0 0 0 3.6.6 1 1 0 0 1 1 1V20a1 1 0 0 1-1 1A17 17 0 0 1 3 4a1 1 0 0 1 1-1h3.5a1 1 0 0 1 1 1c0 1.25.2 2.45.6 3.6a1 1 0 0 1-.25 1z"/></svg>
      Order by Telephone: <strong>(970) 555-0173</strong>
    </div>
    <a class="btn">Order Online</a>
  </div>
  <div class="hero-copy">
    <h1>Fresh Food <em>Fell Good</em></h1>
    <p>We offer a wide variety of American cuisine in a casual, rustic atmosphere.<br>We're offering 16 craft beers on draft, as well as a full service bar with an</p>
  </div>
</header>

<section class="story">
  <h2 class="section-title">Our Story<span class="rule"></span></h2>
  <div class="body">
    <p><b>Lorem ipsum dolor sit amet, consectetur adipiscing elit. Vivamus sed pretium libero. Vivamus facilisis nisi diam.</b> In congue sem dignissim volutpat. Integer vitae neque massa. Sed interdum hendrerit elit nec auctor. Curabitur magna leo accumsan in accumsan at, rhoncus sed dui. Proin elementum scelerisque tortor, at dictum quam sagittis eget. Praesent libero mi, hendrerit a maximus in, congue eu lorem. Vivamus mauris dui, interdum vel turpis eget, tincidunt laoreet est. Quisque scelerisque sem a scelerisque varius.</p>
  </div>
  <a class="btn">More Details</a>
  <div class="photo" role="img" aria-label="Bartender pouring a craft beer from the taps"></div>
</section>

<section class="about">
  <h2 style="left:78px">About Chef</h2>
  <div class="copy left">
    <p>Lorem ipsum dolor sit amet, consectetur adipiscing elit. Suspendisse tincidunt pellentesque facilisis. Suspendisse iaculis ac purus et commodo. Donec hendrerit pharetra sem, at efficitur libero accumsan sed.</p>
    <p>Vestibulum venenatis efficitur feugiat. Cras dolor nisi, luctus ut pharetra vitae, fringilla nec felis. Maecenas egestas mi at ne feugiat fringilla.</p>
  </div>
  <div class="photo" style="left:366px" role="img" aria-label="Portrait of the head chef in whites"></div>
  <div class="photo" style="left:620px" role="img" aria-label="Portrait of the owner in a chef's hat"></div>
  <h2 style="right:74px">About Owner</h2>
  <div class="copy right">
    <p>Lorem ipsum dolor sit amet, consectetur adipiscing elit. Suspendisse tincidunt pellentesque facilisis. Suspendisse iaculis ac purus et commodo. Donec hendrerit pharetra sem, at efficitur libero accumsan sed.</p>
    <p>Vestibulum venenatis efficitur feugiat. Cras dolor nisi, luctus ut pharetra vitae, fringilla nec felis. Maecenas egestas mi at ne feugiat fringilla.</p>
  </div>
</section>

<section class="menu menu-drinks">
  <div class="photo" style="inset:0;opacity:.5;background:linear-gradient(90deg,#d9cbbf,#f4ede6,#d4c3b4)" role="img" aria-label="Faded photo of guests laughing together"></div>
  <h2 class="section-title">Our Menu</h2><span class="rule"></span>
  <div class="cat" style="top:178px">Special Drinks</div>
  <div class="item" style="left:78px;top:240px"><h4>Drink Name 1</h4><p>don't be shy, Colorado original bull fries.. Served with garlic aioli &amp; bloody mary cocktail</p><span class="price">$ 7.99</span></div>
  <div class="item" style="left:78px;top:318px"><h4>Drink Name 2</h4><p>don't be shy, Colorado original bull fries.. Served with garlic aioli &amp; bloody mary cocktail</p><span class="price">$ 9.99</span></div>
  <div class="item" style="left:78px;top:394px"><h4>Drink Name 3</h4><p>don't be shy, Colorado original bull fries.. Served with garlic aioli &amp; bloody mary cocktail</p><span class="price">$ 7.99</span></div>
  <div class="promo" style="left:670px;top:266px;width:450px;height:184px">
    <div class="promo-inner">
      <div class="big">5</div>
      <div class="dollar">$</div>
      <div><h3>THE FIVER HAPPY HOUR</h3><div class="line">MONDAY - FRIDAY, 3-6PM</div><div class="strong">BEER · WINE · COCKTAILS · APPS</div></div>
    </div>
  </div>
  <div class="chevron" style="top:512px"><svg width="16" height="10" viewBox="0 0 16 10"><path d="M2 2l6 6 6-6" stroke="#e0531c" stroke-width="2" fill="none"/></svg></div>
</section>

<section class="menu menu-lunch">
  <div class="cat" style="top:34px">Lunch</div>
  <div class="item" style="left:78px;top:142px"><h4>Pickle Chips</h4><p>fried golden, served with buttermilk ranch</p><span class="price" style="top:4px">$ 7.99</span></div>
  <div class="item" style="left:78px;top:232px"><h4>Cheese Curds</h4><p>beer battered &amp; fried Wisconsin white cheese served with marinara or ranch</p><span class="price">$ 9.99</span></div>
  <div class="item" style="left:78px;top:312px"><h4>Jumbo Pretzel</h4><p>bavarian-style, with honey dijon &amp; queso</p><span class="price" style="top:4px">$ 7.99</span></div>
  <div class="promo" style="left:670px;top:158px;width:450px;height:182px">
    <div class="promo-inner">
      <div class="big">6<small>.99</small></div>
      <div style="margin-left:22px"><h3>YOUNGSTERS OFFER</h3><div class="strong">ALL SELECTIONS (EXCEPT PIZZA) INCLUDE<br>CHOICE SIDE ITEM &amp; A CRÈME SANDWICH COOKIE</div></div>
    </div>
  </div>
  <div class="chevron" style="top:418px"><svg width="16" height="10" viewBox="0 0 16 10"><path d="M2 2l6 6 6-6" stroke="#e0531c" stroke-width="2" fill="none"/></svg></div>
</section>

<section class="menu menu-dinner">
  <div class="cat" style="top:74px">Dinner</div>
  <div class="item" style="left:78px;top:142px"><h4>Buffalo Wings</h4><p>Roostwell, all natural, drums &amp; wings sriracha buffalo / bleu cheese / celery</p><span class="price">$ 7.99</span></div>
  <div class="item" style="left:78px;top:228px"><h4>Mpork Tostadas</h4><p>Pulled pork / fire roasted corn relish cilantro / fresh pico / chipotle ranch</p><span class="price">$ 9.99</span></div>
  <div class="item" style="left:78px;top:314px"><h4>Buffalo Wings</h4><p>Roostwell, all natural, drums &amp; wings sriracha buffalo / bleu cheese / celery</p><span class="price">$ 7.99</span></div>
  <div class="abs" style="left:600px;top:150px;width:1px;height:230px;background:#ddd"></div>
  <div class="item" style="left:640px;top:142px"><h4>Buffalo Wings</h4><p>Roostwell, all natural, drums &amp; wings sriracha buffalo / bleu cheese / celery</p><span class="price">$ 7.99</span></div>
  <div class="item" style="left:640px;top:228px"><h4>Mpork Tostadas</h4><p>Pulled pork / fire roasted corn relish cilantro / fresh pico / chipotle ranch</p><span class="price">$ 9.99</span></div>
  <div class="item" style="left:640px;top:314px"><h4>Buffalo Wings</h4><p>Roostwell, all natural, drums &amp; wings sriracha buffalo / bleu cheese / celery</p><span class="price">$ 7.99</span></div>
  <div class="photo" style="left:0;top:400px;width:330px;height:220px;border-radius:0 50% 40% 0;background:radial-gradient(ellipse at 40% 50%,#c9a06a,#6f8a3a 55%,#fff 72%)" role="img" aria-label="Grilled asparagus and steak plate"></div>
  <div class="photo" style="left:820px;top:420px;width:300px;height:190px;border-radius:50%;background:radial-gradient(ellipse,#b86a33,#8a9a4a 55%,#fff 72%)" role="img" aria-label="Grilled skewers with vegetables"></div>
  <a class="btn">View Details Menu</a>
</section>

<section class="gallery">
  <div class="photo" style="left:0;top:0;background:linear-gradient(135deg,#c48a45,#8a5a2a)" role="img" aria-label="Golden savoury tart"></div>
  <div class="photo" style="left:400px;top:0;background:linear-gradient(135deg,#f1e6d6,#c6303a 60%,#e9d8c0)" role="img" aria-label="Dessert with raspberries"></div>
  <div class="photo" style="left:800px;top:0;background:linear-gradient(135deg,#3a2a1a,#e08a2a 50%,#c23a2a)" role="img" aria-label="Colourful cocktails on the bar"></div>
  <div class="photo" style="left:0;top:334px;background:linear-gradient(135deg,#d6c8b8,#4a4a4a 60%,#8a7a6a)" role="img" aria-label="Stacked dark bread slices"></div>
  <div class="photo" style="left:400px;top:334px;background:linear-gradient(135deg,#5a8a5a,#e8a07a 50%,#c8d8d8)" role="img" aria-label="Salmon with herbs and lime"></div>
  <div class="photo" style="left:800px;top:334px;background:linear-gradient(135deg,#2a2a2a,#7a3a22 50%,#d8d0c8)" role="img" aria-label="Grilled steak on a white plate"></div>
  <div class="gallery-badge"><span class="s">Image</span><span class="l">Gallery</span><span class="m">See More</span></div>
</section>

<section class="features">
  <div class="feature" style="left:78px">
    <svg width="46" height="56" viewBox="0 0 46 56"><path d="M23 2a19 19 0 0 1 19 19c0 14-19 33-19 33S4 35 4 21A19 19 0 0 1 23 2z" fill="none" stroke="#fff" stroke-width="3"/><circle cx="23" cy="21" r="7" fill="none" stroke="#fff" stroke-width="3"/></svg>
    <h3>Our Specialities</h3>
    <p>Private dining room can accommodate 50 people. High quality food, memorable catering service.</p>
  </div>
  <div class="feature" style="left:435px">
    <svg width="64" height="56" viewBox="0 0 64 56"><rect x="10" y="6" width="44" height="32" rx="2" fill="none" stroke="#fff" stroke-width="3"/><path d="M2 46h60l-4 6H6z" fill="#fff"/><path d="M24 26l8-10 8 10" fill="none" stroke="#fff" stroke-width="3"/></svg>
    <h3>Order Online</h3>
    <p>Click here to place your order in minutes.</p>
  </div>
  <div class="feature" style="left:792px">
    <svg width="64" height="56" viewBox="0 0 64 56"><circle cx="40" cy="16" r="12" fill="none" stroke="#fff" stroke-width="3"/><text x="40" y="22" text-anchor="middle" fill="#fff" font-family="Open Sans" font-size="16" font-weight="700">$</text><path d="M4 40h14l12 4h14a4 4 0 0 1 0 8H26" fill="none" stroke="#fff" stroke-width="3"/><path d="M44 46l14-8a4 4 0 0 1 4 6L46 54H4" fill="none" stroke="#fff" stroke-width="3"/></svg>
    <h3>Save &amp; Earn</h3>
    <p>Get card deals, rewards, discounts and vouchers. Here's knowing and happiness with rewards!</p>
  </div>
</section>

<section class="reviews">
  <div class="photo" style="inset:0;opacity:.45;background:linear-gradient(90deg,#cbbcae,#f4efe9,#c6b5a5)" role="img" aria-label="Faded photo of diners enjoying a meal"></div>
  <h2 class="section-title">Customer Reviews</h2><span class="rule"></span>
  <svg class="abs" style="left:468px;top:205px" width="14" height="26" viewBox="0 0 14 26"><path d="M12 2L2 13l10 11" stroke="#999" stroke-width="2" fill="none"/></svg>
  <div class="avatar" role="img" aria-label="Reviewer portrait"></div>
  <svg class="abs" style="left:718px;top:205px" width="14" height="26" viewBox="0 0 14 26"><path d="M2 2l10 11L2 24" stroke="#999" stroke-width="2" fill="none"/></svg>
  <div class="stars">★★★★<span>★</span></div>
  <div class="reviewer">Darren Pollick</div>
  <span class="qmark" style="left:100px;top:378px">“</span>
  <p class="quote">There are many variations of passages of Lorem Ipsum available, but the majority have suffered alteration in some form, by injected humour, or randomised words which don't look even slightly believable.</p>
  <span class="qmark" style="left:1070px;top:410px">”</span>
</section>

<footer class="site-footer">
  <div class="fcol" style="left:78px">
    <h4>Quick Links</h4>
    <ul><li>Home</li><li>About Us</li><li>Our Menu</li><li>Book a Table</li><li>Our Gallery</li><li>Employment</li><li>Private Events</li><li>Contact Us</li></ul>
  </div>
  <div class="fcol" style="left:317px;width:260px">
    <h4>Contact Information</h4>
    <div class="contact-row"><svg width="12" height="16" viewBox="0 0 12 16"><path d="M6 0a6 6 0 0 1 6 6c0 4-6 10-6 10S0 10 0 6a6 6 0 0 1 6-6z" fill="#e0531c"/></svg><span>The Dunlo Hearth &amp; Keg Room<br>2736 Pennick Road<br>Alder Springs, Colorado 80799</span></div>
    <div class="contact-row"><svg width="12" height="12" viewBox="0 0 24 24"><path fill="#e0531c" d="M6.6 10.8a15 15 0 0 0 6.6 6.6l2.2-2.2a1 1 0 0 1 1-.25 11 11 0 0 0 3.6.6 1 1 0 0 1 1 1V20a1 1 0 0 1-1 1A17 17 0 0 1 3 4a1 1 0 0 1 1-1h3.5a1 1 0 0 1 1 1c0 1.25.2 2.45.6 3.6a1 1 0 0 1-.25 1z"/></svg><span>Phone: (970) 555-0173</span></div>
    <div class="contact-row"><svg width="14" height="11" viewBox="0 0 14 11"><rect x=".5" y=".5" width="13" height="10" fill="none" stroke="#e0531c"/><path d="M1 1l6 5 6-5" stroke="#e0531c" fill="none"/></svg><span>info@thedunlokegroom.com</span></div>
  </div>
  <div class="fcol" style="left:634px;width:240px">
    <h4>Newsletter Signup</h4>
    <p>Receive our email address below to receive our FREE newsletter.</p>
    <div class="signup"><span>Your Email</span></div>
    <span class="signup-btn">Subscribe</span>
  </div>
  <div class="fcol follow" style="left:933px">
    <h4>Follow Us</h4>
    <ul><li><i></i>Friendbook</li><li><i></i>WorkLink</li><li><i></i>Chirper</li><li><i></i>Email</li></ul>
  </div>
  <div class="copyright">© 2016 thedunlokegroom.com. All Rights Reserved</div>
</footer>

</body>
</html>
```